INTERNATIONAL SPEAKING BUSINESS FOR WOMEN NEEDS A BROCHURE DESIGN

HEARTHSTONE CIRCLE IS AN INTERNATIONAL FEMALE NETWORK PROVIDING ITS MEMBERS THE UK'S NUMBER ONE RELATIONSHIP SEMINAR FOR WOMEN.
WE ARE ABOUT TO GO LIVE AGAIN AFTER 18 MONTHS AND ONE OF OUR OFFERINGS AT THIS LIVE EVENT, IS OUR BONDWISE WORKSHOP TRACK - AND THIS IS WHERE YOU COME IN :)
IM LOOKING FOR AN ELEGANT, EASY AND WARM TO THE EYE BROCHURE WHICH CAPTURES SOME OF OUR BEST TESTIMONIALS AND CLIENTS. WE HAVE THE LOGO, THE IMAGES AND THE COPY . WE JUST NEED YOUR AMAZING CREATIVE TALENT AND SKILL TO PUT IT ALL TOGETHER TO LOOK ELEGANT AND PROFESSIONAL, YET WELCOMING AND INSPIRING.
OUR IDEAL CLIENT IS A SINGLE, SUCCESSFUL, PROFESSIONAL WOMAN WANTING TO FIND A SOLUTION TO HER RELATIONSHIP CHALLENGES. SHE WANTS TO LET GO OF HER FEARS OF PAST RELATIONSHIPS AND ALIGN WITH AN AMAZING RELATIONSHIP. OUR AIM WITH THE BROCHURE IS TO SHOW THEM WHAT WE DO, HOW WE DO IT AND HOW OUR EXISTING CLIENTS HAVE ALREADY DONE THIS.
THIS IS JUST ONE OF MANY CREATIVE WORKS NEEDED TO BE CARRIED OUT OVER THESE NEXT FEW WEEKS
SO WE ARE LOOKING FOR OUR IDEAL CREATIVE PARTNER ! HOPING TO FIND YOU HERE ;)
hearthstonecircle-example.com
professional, successful women between 30 and 65 looking to resolve their relationship problems
Speaking Business/ Seminars / webinars/ Relationships Coaching for Women
- Similar to logo and website hearthstonecircle-example.com

```html
<!DOCTYPE html>
<html lang="en">
<head>
<meta charset="utf-8">
<title>Hearthstone Circle – Meet the Team</title>
<link rel="stylesheet" href="https://fonts.googleapis.com/css2?family=Montserrat:ital,wght@0,300;0,400;0,700;1,400;1,500&family=Roboto+Condensed:wght@400&display=swap">
<style>
  :root{
    --ink:#111111;
    --paper:#ffffff;
    --pink:#e0466f;
    --blue:#2a6fc9;
    --ring:#5d5d5d;
    --rule:#cfcfcf;
    --sliver:#bdbdbd;
    --stripe-grey:#9a9a9a;
    --text:#2b2b2b;
  }
  *{margin:0;padding:0;box-sizing:border-box}
  html,body{width:1200px;height:849px;overflow:hidden;background:var(--paper)}
  .brochure-page{position:relative;width:1200px;height:849px;overflow:hidden;background:var(--paper);font-family:"Roboto Condensed",Arial,sans-serif;color:var(--text)}

  /* About band */
  .about-band{position:absolute;left:0;top:0;width:1200px;height:192px;background:var(--ink)}
  .about-title{position:absolute;left:75px;top:26px;font-family:"Montserrat",sans-serif;font-style:italic;font-weight:400;font-size:20px;letter-spacing:.4px;color:var(--pink)}
  .about-text{position:absolute;top:57px;font-family:"Montserrat",sans-serif;font-style:italic;font-weight:500;font-size:11.3px;line-height:15.6px;color:var(--paper)}
  .about-text--left{left:75px;width:412px}
  .about-text--right{left:626px;width:300px}
  .founder-art{position:absolute;left:0;top:0}

  /* Team section */
  .team-frame{position:absolute;left:0;top:0}
  .team-heading-mark{position:absolute;left:62px;top:206px}
  .team-heading{position:absolute;left:106px;top:205px;font-family:"Montserrat",sans-serif;font-weight:300;font-size:23px;letter-spacing:.2px;color:var(--ink);background:var(--paper);padding-right:8px}

  .portrait{position:absolute;width:128px;height:128px;border-radius:50%;border:13px solid var(--ring)}
  .portrait--tamsin{left:39px;top:237px;background:radial-gradient(circle at 50% 40%,#f0d9b0,#b98f63)}
  .portrait--philippa{left:1023px;top:223px;background:radial-gradient(circle at 50% 40%,#e4d6c6,#8a6a52)}
  .portrait--rosalind{left:435px;top:442px;background:radial-gradient(circle at 50% 40%,#eedcc0,#a9906f)}
  .portrait--elodie{left:637px;top:455px;background:radial-gradient(circle at 50% 40%,#ddd3c8,#6f625a)}
  .portrait--johanna{left:66px;top:654px;background:radial-gradient(circle at 50% 40%,#d9b597,#7d5a45)}
  .portrait--marisol{left:1023px;top:626px;background:radial-gradient(circle at 50% 40%,#a47a6a,#3a2a2e)}

  .member{position:absolute;font-size:11.8px;line-height:16.3px;font-weight:400}
  .member--right{text-align:right}
  .member--justify p{text-align:justify;text-align-last:right}
  .member-name{font-family:"Montserrat",sans-serif;font-weight:700;font-size:12.8px;line-height:16px;color:#444;letter-spacing:.2px}
  .member-role{font-family:"Montserrat",sans-serif;font-weight:300;font-size:12.8px;line-height:16px;color:#222;letter-spacing:.2px;margin-bottom:2px}

  .member--tamsin{left:208px;top:250px;width:336px}
  .member--philippa{left:686px;top:246px;width:318px}
  .member--rosalind{left:116px;top:426px;width:310px}
  .member--elodie{left:800px;top:451px;width:362px}
  .member--johanna{left:223px;top:663px;width:320px}
  .member--marisol{left:676px;top:652px;width:324px}

  .footer-stripes{position:absolute;left:0;bottom:0}
</style>
</head>
<body>
<main class="brochure-page">

  <section class="about-band">
    <h1 class="about-title">ABOUT LENA MARLOWE</h1>
    <p class="about-text about-text--left">Lena Marlowe is a best-selling author and one of UK’s foremost experts on relationships. A playful, vivacious and inspirational facilitator/ relationship specialist committed to guiding individuals through their journey of self-discovery back to love &amp; peace post painful relationships &amp; events. She is the founder of Hearthstone Circle: UK’s #1 relationship seminar for women. A programme that has changed the lives of thousands of women since 2016. Lena has dedicated the past 10 years working with women to</p>
    <p class="about-text about-text--right">discover how extraordinary they are, to have them know their power and to understand how to be in their relationships with others and most importantly, with themselves post loss or relationship breakups. She has been showing women how to reconnect with their own journey again, whether they are in a marriage, single or separated, she has been gifting this to women throughout the world.</p>
  </section>

  <svg class="founder-art" width="1200" height="240" viewBox="0 0 1200 240">
    <defs>
      <linearGradient id="founderTone" x1="0" y1="0" x2="1" y2="1">
        <stop offset="0" stop-color="#d9b48f"/>
        <stop offset="1" stop-color="#6e4d3a"/>
      </linearGradient>
    </defs>
    <polygon points="1040,178 1058,178 1100,222 1082,222" fill="var(--sliver)"/>
    <polygon points="943,16 962,16 1058,180 1039,180" fill="var(--pink)"/>
    <g role="img" aria-label="Portrait photograph of founder Lena Marlowe">
      <polygon points="970,16 1200,16 1200,180 1066,180" fill="url(#founderTone)"/>
    </g>
  </svg>

  <svg class="team-frame" width="1200" height="849" viewBox="0 0 1200 849" aria-hidden="true">
    <polyline points="62,201 1062,201 1183,262 1183,824 62,824 62,201" fill="none" stroke="var(--rule)" stroke-width="1"/>
  </svg>
  <svg class="team-heading-mark" width="48" height="20" viewBox="0 0 48 20" aria-hidden="true">
    <polygon points="0,0 40,0 48,20 8,20" fill="var(--pink)"/>
  </svg>
  <h2 class="team-heading">MEET THE REST OF THE TEAM</h2>

  <div class="portrait portrait--tamsin" role="img" aria-label="Portrait photograph of Tamsin Okafor"></div>
  <article class="member member--tamsin">
    <div class="member-name">TAMSIN OKAFOR, 34,</div>
    <div class="member-role">MISSING AND EXPLOITATION COORDINATOR.</div>
    <p>I joined Hearthstone Circle to solve issues I had in my relationships with men that I had been carrying for a long time. As a result of this work I can see things from a different perspective. The conversation that once dominated in my mind about relationships is no longer there, no longer holding me back, I feel free now. This has been a life changing experience of which I am eternally grateful.</p>
  </article>

  <div class="portrait portrait--philippa" role="img" aria-label="Portrait photograph of Philippa"></div>
  <article class="member member--right member--philippa">
    <div class="member-name">PHILIPPA, 42,</div>
    <div class="member-role">HAIRSTYLIST</div>
    <p>Masterclasses have been a fantastic way of consolidating Lena’s teaching in my mind after the weekends. It has been a great way to keep consistency in the tools which are disciplines that I very much need to shift my mindset. Through the questions and answers, I can see practical ways in which others are applying the teaching. I gain insights into my own addictions and unhelpful thinking through asking questions to Lena, taking her advice, participating and appreciating the courage and insight of the other HC tribe members.</p>
  </article>

  <div class="portrait portrait--rosalind" role="img" aria-label="Portrait photograph of Rosalind Pyke"></div>
  <article class="member member--right member--justify member--rosalind">
    <div class="member-name">ROSALIND PYKE, 63,</div>
    <div class="member-role">MIDWIFE LABOUR WARD.</div>
    <p>“I honestly didn’t know how this was going to help me get through the pain of my marriage breakup. Then one evening something in the message landed. Lena was talking about recognising and letting the emotions burn through and that absolutely resonated with me…I continued with the classes in the hope of somehow finding a way out of this pain. I began applying the tools being taught which really helped just to give me space and time in the day to find me, and thanks to this I began to have my breakthrough. A few weeks after, I started to see a real shift in me. I started to see that I could begin to heal. I started to feel a sense of peace and that I was able to manage these huge emotions. I’ve loved every minute of it.”</p>
  </article>

  <div class="portrait portrait--elodie" role="img" aria-label="Portrait photograph of Elodie Varenne"></div>
  <article class="member member--elodie">
    <div class="member-name">ELODIE VARENNE, 33,</div>
    <div class="member-role">SENIOR CUSTOMER SUCCESS MANAGER</div>
    <p>Masterclasses are like Mini mastery weekends, absolutely life changing. I’ve finally realised why I keep reliving patterns of behaviour like comparison, feeling worthless or stupid and it’s because I haven’t dealt with deep down emotions that I have learnt to suppress since I was young. I now have the tools to see these emotions as they come up and process them instead of ignoring or suppressing them. I’m finally ready to love and accept myself for who I am.</p>
  </article>

  <div class="portrait portrait--johanna" role="img" aria-label="Portrait photograph of Johanna Kessel"></div>
  <article class="member member--johanna">
    <div class="member-name">JOHANNA KESSEL, 39,</div>
    <div class="member-role">RECEPTIONIST FOR ADULT MENTAL HEALTH</div>
    <p>I feel incredibly lucky to have found this group of amazing women. The masterclass series and network has opened my eyes to how I treat myself, my thoughts, my emotions, and my mindset in general. The masterclasses have gifted me in depth information and tools to put in place to break my trauma &amp; addiction cycles. I have learnt to give myself more compassion &amp; self-love.</p>
  </article>

  <div class="portrait portrait--marisol" role="img" aria-label="Portrait photograph of Marisol Quintero"></div>
  <article class="member member--right member--marisol">
    <div class="member-name">MARISOL QUINTERO, 38,</div>
    <div class="member-role">DIRECTOR OF LUXURY SALES</div>
    <p>The Masterclass series is my most important weekly date with myself! They involve a deeper learning of all the tools. Having the chance to go through each of them in detail, allows me to engage in the benefit of practicing them each day. Also, it is so powerful to learn about the Senior members and their journeys and how they have incorporated the tools to become safer within themselves.</p>
  </article>

  <svg class="footer-stripes" width="420" height="14" viewBox="0 0 420 14" aria-hidden="true">
    <polygon points="0,0 84,0 90,14 0,14" fill="var(--stripe-grey)"/>
    <polygon points="84,0 275,0 281,14 90,14" fill="var(--blue)"/>
    <polygon points="275,0 385,0 391,14 281,14" fill="var(--pink)"/>
  </svg>

</main>
</body>
</html>
```